New Toothpaste brand needs a logo & packaging design

Our company is launching a new toothpaste and is looking for a logo and packaging design. The toothpaste brand is called Brivana. The packaging should have the same design quality as the major international brands, such as Lumora, Lumora Totalcare, Dentiva, Pexolo, Wind-rise, Marvest, etc. The dominant colors for our brand should be hues of blue, similar to other major brands. In addition, there should be a little bit of green to represent the "Fresh Mint Blast" flavor and the "Extracts of Aloe Vera" included in the ingredients.

There are typically 3 unique sides on a toothpaste box:

The face: Repeated on ~3 sides of the 4 faces of the box
The back: The 4th box face has the instructions for use, ingredients, company information, bar code/product info, and some branding elements.
The sides: Usually consisting of just the logo, flavor etc.

Please refer to existing brands such as Lumora, Lumora Total-care, and Dentiva for an example of typical box layout and elements.

Task Details:
Package Dimensions: 180 mm x 48 mm x 28 mm, 100 ml toothpaste tube
Brand Name: Brivana
Description: Fluoride Toothpaste
Flavor: Fresh Mint Blast
5 Actions: Protects against cavities and tartar, freshens breath, whitens teeth, and maintains healthy gums. These actions can also be made into a list like Lumora Total Care or Dentiva Max care. For instance, Strong Teeth, Fresh Breath, Whitening, Healthy Gums, Cavity and Tartar Protection.
Also contains whitening micro particles and extracts of aloe vera which may be highlighted on the package

Overall, the look should be high quality and with the same look and feel as the big brands mentioned previously. We do not have an existing logo for this brand. The face of the package is the most important element as it is often repeated on several sides and on the tube itself.

Please let me know if you have any questions.

I've attached some of our favorite big brand designs below. I would say the Lumora Total Care and Gleam vers

The logos I've seen so far for Brivana, have been a bit too bold. A little bold is okay, but just needs to be moderate. 

I would like the colors to be bright and appealing. I mentioned shades of blue being the major color, but green should also be highlighted as well, perhaps in a 80% blue to 20% green ratio. 

Target Market(s)

adult consumer of toothpaste, both female and male.

Industry/Entity Type

It Company

Requirements
Must have
• A logo with the brand name: Brivana
Description or sub text: Fluoride Toothpaste
Flavor: Fresh Mint Blast
A phrase or list describing the Toothpaste Actions: e.g., Protects against cavities and tartar, freshens breath, whitens teeth, and maintains healthy gums. Or as a list simialr to Lumora Total Care or Dentiva Max Care:
-Anti-cavity
-Anti-tartar
-Fresh breath
-Whitening
-Healthy Gums

Special ingredient of "whitening micro particles: and "extracts of aloe vera", which should also be highlighted.

The color should mostly be shades of blue, with only a little bit of green to accentuate the fresh mint blast flavor and aloe vera

Nice to have
• The design should really look good next to lumora total care, gleam pure, and dentiva max care. These are our favorite designs.
Should not have
• For aloe vera, there is no need to show the plant.

The Brivana logo shouldn't be too Bold. This should be appeal to all consumers, not just men.

```html
<!DOCTYPE html>
<html lang="en">
<head>
<meta charset="utf-8">
<title>Brivana Fluoride Toothpaste – Box Artwork</title>
<link rel="stylesheet" href="https://fonts.googleapis.com/css2?family=Arimo:wght@400;700&display=swap">
<style>
  :root {
    --page-bg: #ffffff;
    --blue-deep: #14448c;
    --blue-mid: #1d5cab;
    --blue-bright: #2f86dc;
    --green-main: #5fae2e;
    --green-light: #8cd04f;
    --green-dark: #3f8a1e;
    --ink-blue: #123f88;
    --red-tab: #d01c1c;
    --white: #ffffff;
  }
  * { margin: 0; padding: 0; box-sizing: border-box; }
  html, body {
    width: 1200px; height: 961px; overflow: hidden;
    background: var(--page-bg);
    font-family: "Arimo", Arial, sans-serif;
  }
  .dieline {
    position: absolute; left: 20px; top: 348px;
    width: 1117px; height: 255px;
    transform: scale(1.0385); transform-origin: 0 0;
    color: var(--white);
  }
  .panel { position: absolute; top: 0; height: 255px; overflow: hidden; }

  /* Front face */
  .front {
    left: 0; width: 715px;
    background: linear-gradient(180deg, var(--blue-mid) 0%, var(--blue-deep) 100%);
  }
  .benefit-column {
    position: absolute; left: 565px; top: 0; width: 150px; height: 255px; z-index: 1;
    background: linear-gradient(90deg, rgba(47,134,220,0) 0%, var(--blue-bright) 55%, var(--blue-mid) 100%);
  }
  .benefit-list {
    position: absolute; right: 12px; top: 12px;
    list-style: none; text-align: right; font-size: 13px; letter-spacing: 0.3px;
  }
  .benefit-list li { height: 38px; line-height: 14px; white-space: nowrap; }
  .front-brand {
    position: absolute; left: 62px; top: 74px; z-index: 2;
    font-size: 78px; font-weight: 700; letter-spacing: 1px; line-height: 1;
  }
  .front-desc {
    position: absolute; left: 165px; top: 178px; z-index: 2;
    font-size: 17px; letter-spacing: 0.5px;
  }
  .volume-pill {
    position: absolute; left: 0; top: 227px; width: 68px; height: 15px; z-index: 2;
    background: var(--green-main); border-radius: 0 8px 8px 0;
    font-size: 12px; line-height: 15px; padding-left: 6px;
  }
  .claims {
    position: absolute; left: 0; top: 229px; width: 715px; height: 16px; z-index: 2;
    font-size: 13px; letter-spacing: 0.3px;
  }
  .claims span { position: absolute; top: 0; white-space: nowrap; }
  .tooth-badge {
    position: absolute; left: 505px; top: 0; width: 57px; height: 67px; z-index: 2;
    background:
      radial-gradient(ellipse 16px 20px at 50% 48%, #ffffff 0%, #eef6ea 55%, rgba(255,255,255,0) 100%),
      linear-gradient(180deg, var(--green-light), var(--green-main));
    border-radius: 0 0 6px 6px; border: 1px solid rgba(255,255,255,0.6); border-top: none;
  }

  .divider {
    position: absolute; left: 715px; top: 0; width: 8px; height: 255px;
    background: linear-gradient(90deg, var(--green-main) 0 3px, var(--white) 3px 5px, var(--green-main) 5px);
  }

  /* Ingredient face */
  .ingredients {
    left: 723px; width: 242px;
    background: linear-gradient(180deg, var(--green-light) 0%, var(--green-main) 60%, var(--green-dark) 100%);
    text-align: center;
  }
  .ingredients .line { position: absolute; left: 0; width: 100%; line-height: 1; }
  .caption { font-size: 13px; }
  .feature-white { font-size: 16px; }
  .feature-blue { font-size: 17px; color: var(--ink-blue); }
  .aloe-oval { position: absolute; left: 46px; top: 39px; }
  .new-tab {
    position: absolute; left: 190px; top: 0; width: 52px; height: 24px;
    background: var(--red-tab); border-radius: 0 0 0 6px;
    font-size: 13px; line-height: 24px;
  }

  /* Side face */
  .side {
    left: 965px; width: 152px;
    background: linear-gradient(180deg, var(--blue-mid), var(--blue-deep));
  }
  .side-volume {
    position: absolute; left: 32px; top: 0; width: 16px; height: 65px;
    background: var(--green-main);
  }
  .side-volume span {
    position: absolute; left: 50%; top: 50%;
    transform: translate(-50%, -50%) rotate(-90deg);
    font-size: 11px; white-space: nowrap;
  }
  .side-brand, .side-desc {
    position: absolute; white-space: nowrap;
    transform: translate(-50%, -50%) rotate(-90deg);
  }
  .side-brand { left: 96px; top: 135px; font-size: 56px; font-weight: 700; letter-spacing: 1px; }
  .side-desc { left: 140px; top: 95px; font-size: 13px; }
</style>
</head>
<body>
  <main class="dieline">
    <section class="panel front" aria-label="Front face">
      <div class="benefit-column">
        <ul class="benefit-list">
          <li>ANTI-CAVITY</li>
          <li>ANTI-TARTAR</li>
          <li>FRESH BREATH</li>
          <li>WHITENING</li>
          <li>HEALTHY GUMS</li>
        </ul>
      </div>
      <div class="front-brand">Brivana</div>
      <div class="front-desc">FLUORIDE TOOTHPASTE</div>
      <div class="volume-pill">100 ML</div>
      <div class="claims">
        <span style="left:148px">FRESHENS BREATH</span>
        <span style="left:325px">WHITENS TEETH</span>
        <span style="left:481px">MAINTAINS HEALTHY GUMS</span>
      </div>
      <div class="tooth-badge" role="img" aria-label="Glossy white tooth illustration on a green badge"></div>
    </section>

    <div class="divider"></div>

    <section class="panel ingredients" aria-label="Ingredient face">
      <div class="line caption" style="top:14px">EXTRACTS OF</div>
      <svg class="aloe-oval" width="150" height="42" viewBox="0 0 150 42">
        <ellipse cx="75" cy="21" rx="74" ry="20" fill="#7cc244" stroke="#ffffff" stroke-opacity="0.6"/>
        <text x="75" y="28" text-anchor="middle" font-family="Arimo, Arial, sans-serif" font-size="19" fill="#123f88">ALOE VERA</text>
      </svg>
      <div class="line caption" style="top:116px">FLAVOR</div>
      <div class="line feature-white" style="top:130px">FRESH</div>
      <div class="line feature-blue" style="top:152px">MINT BLAST</div>
      <div class="line caption" style="top:190px">WHITENING</div>
      <div class="line feature-blue" style="top:205px">MICRO</div>
      <div class="line feature-blue" style="top:228px">PARTICLES</div>
      <div class="new-tab">NEW</div>
    </section>

    <section class="panel side" aria-label="Side face">
      <div class="side-volume"><span>100 ML</span></div>
      <div class="side-brand">Brivana</div>
      <div class="side-desc">FLUORIDE TOOTHPASTE</div>
    </section>
  </main>
</body>
</html>
```